Trade Show Booth Sign Design for Retracting Banner

I need a trade show booth sign designed. It will be for a retractable banner that is double sided with 34 by 81 inch.

I want to incorporate my logo (see attached, have it in other file formats as well) and graphics from my website (https://www.dolbrookteachingadvisory.com/) with parts or all of the following text.

· Educational Content Creation
o Supplemental Textbook Content Development
o E-learning Content Development
· Curriculum Development
o KVTR/Bright Ladder
o Three Dimensional Learning
· Assessment
o Formative Assessments
o Elementary School, Middle School, High School, College, and Business
· Professional Development
o Training
o Facilitation

Target Market(s)

Education

Industry/Entity Type

Education

Font styles to use
Sans Serif

Colors

Designer to choose colors to be used in the design.

Requirements
Must have
• Eye catching and easy to read design
Nice to have
• Would like to see incorporation of my logo and some of the elements of my website images
Should not have
• N/A

```html
<!DOCTYPE html>
<html lang="en">
<head>
<meta charset="utf-8">
<title>Dolbrook Teaching Advisory – Retractable Banner</title>
<link rel="stylesheet" href="https://fonts.googleapis.com/css2?family=Fira+Sans+Extra+Condensed:wght@400;600;700;800&display=swap">
<style>
  :root {
    --navy: #0f2a6b;
    --navy-soft: #1d3c8a;
    --sky: #8fd2ec;
    --steel: #5a9ec4;
    --pale: #eaf5fb;
    --art: #dce9f4;
    --white: #ffffff;
    --stage: #d6d6d6;
  }
  * { margin: 0; padding: 0; box-sizing: border-box; }
  html, body {
    width: 1200px; height: 1200px; overflow: hidden;
    background: var(--stage);
    font-family: "Fira Sans Extra Condensed", sans-serif;
  }
  .banner {
    position: absolute; left: 376px; top: 44px;
    width: 448px; height: 1112px;
    background: var(--white);
    overflow: hidden;
    box-shadow: 0 6px 24px rgba(0,0,0,0.18);
  }
  .banner-shapes { position: absolute; inset: 0; }
  .brand {
    position: absolute; left: 0; top: 186px; width: 448px;
    text-align: center; color: var(--navy); font-weight: 800;
  }
  .brand-name { font-size: 86px; line-height: 1; letter-spacing: 1px; }
  .brand-sub { font-size: 27px; line-height: 1.1; letter-spacing: 0.5px; }
  .service { position: absolute; left: 140px; width: 294px; }
  .service-title {
    position: relative; height: 30px; border-radius: 15px;
    background: var(--navy); color: var(--white);
    font-weight: 700; font-size: 18px; line-height: 30px;
    padding-left: 36px; padding-right: 10px;
    white-space: nowrap; overflow: hidden;
  }
  .service-title::before {
    content: ""; position: absolute; left: 2px; top: 2px;
    width: 26px; height: 26px; border-radius: 50%;
    background: var(--sky);
  }
  .service-list {
    list-style: none; margin: 12px 0 0 32px;
    border-left: 1.5px solid var(--steel);
    color: var(--navy); font-size: 18px; line-height: 25px;
  }
  .service-list li { position: relative; padding-left: 8px; }
  .service-list li::before {
    content: ""; position: absolute; left: -5px; top: 9px;
    width: 8px; height: 8px; border-radius: 50%; background: var(--navy);
  }
  .web {
    position: absolute; left: 0; top: 1042px; width: 448px;
    color: var(--navy); font-weight: 700;
  }
  .web-prefix { position: absolute; left: 48px; font-size: 24px; }
  .web-address { position: absolute; left: 128px; font-size: 25px; }
</style>
</head>
<body>
  <main class="banner">
    <svg class="banner-shapes" width="448" height="1112" viewBox="0 0 448 1112" xmlns="http://www.w3.org/2000/svg">
      <defs>
        <linearGradient id="bulbGlow" x1="0" y1="0" x2="1" y2="0">
          <stop offset="0" stop-color="#0f2a6b"/>
          <stop offset="0.5" stop-color="#1d3c8a"/>
          <stop offset="1" stop-color="#0f2a6b"/>
        </linearGradient>
      </defs>
      <polygon class="doodle-field" points="0,100 448,100 448,308 224,370 0,308" fill="var(--pale)" role="img" aria-label="Faint line drawings of school supplies, clocks and books"/>
      <polygon class="top-chevron" points="0,0 448,0 448,118 224,178 0,118" fill="var(--navy)"/>
      <rect class="bulb-row" x="14" y="6" width="420" height="104" rx="4" fill="url(#bulbGlow)" role="img" aria-label="Row of hanging crumpled-paper light bulbs in red, blue, yellow, orange and light blue"/>
      <rect class="idea-art" x="0" y="400" width="150" height="712" fill="var(--art)" role="img" aria-label="Drawn heads with light bulbs rising from a laboratory flask"/>
      <polygon class="band-sky" points="0,308 224,370 224,440 0,405" fill="var(--sky)"/>
      <polygon class="band-steel" points="120,398 224,370 224,440" fill="var(--steel)"/>
      <polygon class="band-navy" points="224,370 448,308 448,375 224,436" fill="var(--navy)"/>
      <polygon class="corner-sky" points="448,982 448,1112 230,1112" fill="var(--sky)"/>
      <polygon class="corner-navy" points="230,1112 296,1074 296,1112" fill="var(--navy)"/>
      <polygon class="corner-steel" points="296,1074 340,1112 296,1112" fill="var(--steel)"/>
    </svg>

    <header class="brand">
      <div class="brand-name">DOLBROOK</div>
      <div class="brand-sub">Teaching Advisory</div>
    </header>

    <section class="service" style="top:497px">
      <h2 class="service-title">EDUCATIONAL CONTENT CREATION</h2>
      <ul class="service-list">
        <li>Supplemental Textbook Content Development</li>
        <li>E-learning Content Development</li>
      </ul>
    </section>

    <section class="service" style="top:643px">
      <h2 class="service-title">CURRICULUM DEVELOPMENT</h2>
      <ul class="service-list">
        <li>KVTR/Bright Ladder</li>
        <li>Three Dimensional Learning</li>
      </ul>
    </section>

    <section class="service" style="top:764px">
      <h2 class="service-title">ASSESSMENT</h2>
      <ul class="service-list">
        <li>Formative Assessments</li>
        <li>Elementary School, Middle School, High School, College, and Business</li>
      </ul>
    </section>

    <section class="service" style="top:908px">
      <h2 class="service-title">PROFESSIONAL DEVELOPMENT</h2>
      <ul class="service-list">
        <li>Training</li>
        <li>Facilitation</li>
      </ul>
    </section>

    <footer class="web">
      <span class="web-prefix">www</span>
      <span class="web-address">dolbrookteachingadvisory.com</span>
    </footer>
  </main>
</body>
</html>
```